Business Card - Professional Minimalist - Double sided

We appreciate minimalist logo/web/collateral designs that allow design to tell a story. We want to relay a professional image/approach but throwing in a splash of modern when we’re able so long as it’s not distracting. Think 75% classic corporate, 25% modern. Open to black or white design, not sure which might look the best.

Target Market(s)

Senior executives or related government affairs contacts within the agriculture, energy, and defense industries (i.e., potential clients) but located outside of Washington, DC. Most potential clients based in DC with be familiar with both of us and our shared history.

Industry/Entity Type

Consulting

Contact Information for Business Card

Name: Daniel R. Whitlock
Title: Co-Founder & Partner
Address: 418 Bramblewood Ave. SE | Suite 2716 | Washington, D.C. 20019
Phone: (202) 555-0187
Email: Daniel@HollerbyWhitlock.com

Font styles to use
Serif

Colors

Designer to choose only greyscale colors for use in the design.

Requirements
Must have
• Name: Daniel R. Whitlock
Phone: (202) 555-0187

```html
<!DOCTYPE html>
<html lang="en">
<head>
<meta charset="utf-8">
<title>Hollerby Whitlock Group – Business Card</title>
<link href="https://fonts.googleapis.com/css2?family=Noto+Serif:wght@400;700&display=swap" rel="stylesheet">
<style>
  :root {
    --backdrop: #1c1c1c;
    --card-dark: #555557;
    --card-light: #ffffff;
    --ink-dark: #4a4a4c;
    --ink-mid: #6d6d70;
    --ink-soft: #a4a5a8;
    --rule-light: #c9c9cb;
    --white: #ffffff;
  }
  * { margin: 0; padding: 0; box-sizing: border-box; }
  html, body {
    width: 1200px; height: 988px; overflow: hidden;
    background: var(--backdrop);
    font-family: "Noto Serif", Georgia, serif;
  }
  .canvas { position: relative; width: 1200px; height: 988px; }

  .card {
    position: absolute; width: 560px; height: 320px;
    border-radius: 22px; overflow: hidden;
  }

  /* Back side */
  .card--back { left: 70px; top: 120px; background: var(--card-dark); }
  .card--back .brand {
    position: absolute; left: 0; right: 0; top: 134px;
    display: flex; align-items: center; justify-content: center; gap: 14px;
  }
  .brand__square { width: 26px; height: 26px; background: var(--white); }
  .card--back .brand__name {
    color: var(--white); font-size: 25px; letter-spacing: 2px;
    text-transform: uppercase; font-weight: 400;
  }
  .card--back .brand-rule {
    position: absolute; left: 120px; right: 120px; top: 186px;
    height: 1px; background: rgba(255,255,255,0.55);
  }

  /* Front side */
  .card--front { left: 570px; top: 548px; background: var(--card-light); }
  .front__brand {
    position: absolute; left: 34px; top: 38px;
    color: var(--ink-dark); font-size: 17px; letter-spacing: 1.5px;
    text-transform: uppercase;
  }
  .front__rule {
    position: absolute; left: 34px; top: 70px; width: 236px;
    height: 1px; background: var(--rule-light);
  }
  .front__mark-area {
    position: absolute; right: 40px; top: 40px; width: 150px; height: 150px;
    background: #d9d9db;
  }
  .contact {
    position: absolute; left: 52px; top: 108px;
    color: var(--ink-mid); font-size: 12.5px; line-height: 1.35;
  }
  .contact__accent {
    position: absolute; left: 34px; top: 113px; width: 8px; height: 26px;
    background: var(--ink-dark);
  }
  .contact__name {
    color: var(--ink-dark); font-weight: 700; font-size: 18px;
    text-transform: uppercase; letter-spacing: 0.5px;
  }
  .contact__title { margin-bottom: 10px; }
  .contact__address { margin-bottom: 10px; }
  .contact__line { display: flex; align-items: center; gap: 8px; }
  .contact__line svg { width: 12px; height: 12px; fill: var(--ink-dark); flex: none; }
</style>
</head>
<body>
<main class="canvas">

  <section class="card card--back" aria-label="Card back">
    <div class="brand">
      <span class="brand__square"></span>
      <span class="brand__name">Hollerby Whitlock Group</span>
    </div>
    <div class="brand-rule"></div>
  </section>

  <section class="card card--front" aria-label="Card front">
    <div class="front__brand">Hollerby Whitlock Group</div>
    <div class="front__rule"></div>
    <div class="front__mark-area" role="img" aria-label="Company emblem area"></div>

    <div class="contact__accent"></div>
    <div class="contact">
      <div class="contact__name">Daniel R. Whitlock</div>
      <div class="contact__title">Co-Founder &amp; Partner</div>
      <div class="contact__address">
        418 Bramblewood Ave. SE<br>
        Suite 2716<br>
        Washington, D.C. 20019
      </div>
      <div class="contact__line">
        <svg viewBox="0 0 24 24" aria-hidden="true"><path d="M6.6 10.8a15 15 0 0 0 6.6 6.6l2.2-2.2c.3-.3.7-.4 1-.2 1.1.4 2.3.6 3.6.6.6 0 1 .4 1 1V20c0 .6-.4 1-1 1A17 17 0 0 1 3 4c0-.6.4-1 1-1h3.5c.6 0 1 .4 1 1 0 1.3.2 2.5.6 3.6.1.3 0 .7-.2 1z"/></svg>
        <span>(202) 555-0187</span>
      </div>
      <div class="contact__line">
        <svg viewBox="0 0 24 24" aria-hidden="true"><path d="M2 5h20v14H2z M2 5l10 8 10-8" stroke="#fff" stroke-width="1.5"/></svg>
        <span>Daniel@HollerbyWhitlock.com</span>
      </div>
      <div class="contact__line">
        <svg viewBox="0 0 24 24" aria-hidden="true"><circle cx="12" cy="12" r="10"/><path d="M2 12h20M12 2c3 3 3 17 0 20M12 2c-3 3-3 17 0 20" stroke="#fff" stroke-width="1.3" fill="none"/></svg>
        <span>www.HollerbyWhitlock.com</span>
      </div>
    </div>
  </section>

</main>
</body>
</html>
```